Business card design needed

I need a business card for my new Food & Lifestyle Coaching business - "Bloomwell Food & Lifestlye Coaching"

i already have a logo and would like to have that incorporated into the business card, obviously.

i would like a design that says "fresh" and "funky" - my target market is female, aged 20-45 so i want something that will stand out to them when they see it.

My "Company Colour" is Apple Green
Updates

Thankyou to everyone who has submitted a design for my project. At this stage i have quite a large number of designs to chose from and with only a short time until my project closes i am focusing now on chosing from those i have already shortlisted so am unfortunately not considering any new desings.

Thankyou again for your interest in my project.

Target Market(s)

Female, Health Conscious (or looking to improve their health/lifestyle), aged between 20-45

Industry/Entity Type

Business

Contact Information for Business Card

Tessa Harlow
Ph: 0438215790
Email: hellobloom@quarlmail.com

Requirements
Must have
• Must include my existing Logo
Nice to have
• Would be nice to incoirporate and appointment card on the back

```html
<!DOCTYPE html>
<html lang="en">
<head>
<meta charset="utf-8">
<title>Bloomwell Food &amp; Lifestyle Coaching – Business &amp; Appointment Card</title>
<link href="https://fonts.googleapis.com/css2?family=Open+Sans:wght@400;600;700&family=Sacramento&display=swap" rel="stylesheet">
<style>
  :root {
    --apple-green: #7cbf38;
    --apple-green-light: #95cf4a;
    --apple-green-dark: #5fa42c;
    --pattern-green: #86c443;
    --ink: #2b2b2b;
    --grey: #555555;
    --white: #ffffff;
    --sunday-red: #e0312f;
    --backdrop: #e8e4df;
  }
  * { box-sizing: border-box; margin: 0; padding: 0; }
  html, body {
    width: 1200px;
    height: 867px;
    overflow: hidden;
    background: var(--backdrop);
    font-family: "Open Sans", Arial, sans-serif;
  }
  .card {
    position: absolute;
    top: 278px;
    width: 520px;
    height: 312px;
    border-radius: 14px;
    overflow: hidden;
    background: var(--white);
    box-shadow: 0 6px 18px rgba(0,0,0,0.18);
    display: flex;
  }
  .card--front { left: 50px; }
  .card--back { left: 630px; }

  /* Brand lockup */
  .brand { display: flex; flex-direction: column; align-items: center; }
  .brand__name {
    font-family: "Sacramento", cursive;
    color: var(--ink);
    line-height: 1;
    display: flex;
    align-items: center;
    gap: 8px;
    white-space: nowrap;
  }
  .brand__dot {
    border-radius: 50%;
    background: var(--apple-green);
    display: inline-block;
    flex: none;
  }
  .brand__tagline {
    font-size: 10px;
    color: var(--ink);
    letter-spacing: 0.2px;
    border-top: 2px dotted var(--apple-green);
    padding-top: 3px;
    white-space: nowrap;
  }

  /* Front */
  .front__logo-side {
    width: 270px;
    padding: 0 24px;
    display: flex;
    align-items: center;
    justify-content: center;
  }
  .front__logo-side .brand__name { font-size: 44px; }
  .front__logo-side .brand__dot { width: 18px; height: 18px; }
  .front__contact-side {
    flex: 1;
    background: linear-gradient(160deg, var(--apple-green-light), var(--apple-green-dark));
    color: var(--white);
    padding: 66px 22px 0 26px;
  }
  .contact__name {
    font-family: "Sacramento", cursive;
    font-size: 34px;
    color: var(--ink);
    line-height: 1;
    text-align: center;
    white-space: nowrap;
  }
  .contact__rule {
    border-top: 2px dotted rgba(255,255,255,0.85);
    margin: 22px 0 34px;
  }
  .contact__phone {
    font-family: "Sacramento", cursive;
    font-size: 25px;
    line-height: 1.2;
    white-space: nowrap;
  }
  .contact__email {
    font-family: "Sacramento", cursive;
    font-size: 21px;
    line-height: 1.3;
    white-space: nowrap;
  }

  /* Back */
  .back__pattern {
    width: 196px;
    background: linear-gradient(150deg, var(--apple-green-light), var(--pattern-green) 60%, var(--apple-green));
  }
  .back__form {
    flex: 1;
    padding: 22px 22px 0 24px;
    display: flex;
    flex-direction: column;
    align-items: center;
  }
  .back__form .brand__name { font-size: 36px; }
  .back__form .brand__dot { width: 13px; height: 13px; }
  .back__form .brand__tagline { font-size: 8px; }
  .form__rule {
    width: 100%;
    border-top: 2px dotted var(--grey);
    margin-top: 34px;
  }
  .form__label {
    color: var(--apple-green);
    font-weight: 600;
    font-size: 12px;
    margin-top: 14px;
  }
  .weekdays {
    list-style: none;
    display: flex;
    justify-content: space-between;
    width: 100%;
    margin-top: 12px;
    padding: 0 6px;
  }
  .weekday {
    display: flex;
    flex-direction: column;
    align-items: center;
    gap: 5px;
    font-weight: 700;
    font-size: 12px;
    color: var(--apple-green);
  }
  .weekday__mark {
    width: 18px;
    height: 18px;
    border-radius: 50%;
    border: 2px solid var(--grey);
  }
  .weekday--sunday { color: var(--sunday-red); }
  .booking {
    width: 100%;
    display: flex;
    align-items: flex-end;
    gap: 8px;
    margin-top: 10px;
  }
  .booking__field {
    flex: 1;
    display: flex;
    flex-direction: column;
    align-items: center;
  }
  .booking__line {
    width: 100%;
    border-top: 2px dotted var(--grey);
    margin-bottom: 5px;
  }
  .booking__caption {
    color: var(--apple-green);
    font-weight: 600;
    font-size: 12px;
  }
  .booking__at {
    font-weight: 700;
    font-size: 11px;
    color: var(--grey);
    align-self: center;
    margin-bottom: 14px;
  }
  .booking__meridiem {
    font-weight: 700;
    font-size: 11px;
    color: var(--grey);
    line-height: 1.2;
    margin-bottom: 22px;
  }
</style>
</head>
<body>

<section class="card card--front" aria-label="Business card front">
  <div class="front__logo-side">
    <div class="brand">
      <span class="brand__name"><span class="brand__dot"></span>Bloomwell</span>
      <span class="brand__tagline">Food &amp; Lifestyle Coaching</span>
    </div>
  </div>
  <div class="front__contact-side">
    <p class="contact__name">Tessa Harlow</p>
    <div class="contact__rule"></div>
    <p class="contact__phone">0438 215 790</p>
    <p class="contact__email">hellobloom@quarlmail.com</p>
  </div>
</section>

<section class="card card--back" aria-label="Appointment card back">
  <div class="back__pattern" role="img" aria-label="Repeating pattern of light green leaf-wing shapes on apple green"></div>
  <div class="back__form">
    <div class="brand">
      <span class="brand__name"><span class="brand__dot"></span>Bloomwell</span>
      <span class="brand__tagline">Food &amp; Lifestyle Coaching</span>
    </div>
    <div class="form__rule"></div>
    <p class="form__label">Has an appointment on</p>
    <ul class="weekdays">
      <li class="weekday"><span class="weekday__mark"></span>M</li>
      <li class="weekday"><span class="weekday__mark"></span>T</li>
      <li class="weekday"><span class="weekday__mark"></span>W</li>
      <li class="weekday"><span class="weekday__mark"></span>T</li>
      <li class="weekday"><span class="weekday__mark"></span>F</li>
      <li class="weekday"><span class="weekday__mark"></span>S</li>
      <li class="weekday weekday--sunday"><span class="weekday__mark"></span>S</li>
    </ul>
    <div class="booking">
      <div class="booking__field">
        <span class="booking__line"></span>
        <span class="booking__caption">Date</span>
      </div>
      <span class="booking__at">AT</span>
      <div class="booking__field">
        <span class="booking__line"></span>
        <span class="booking__caption">Time</span>
      </div>
      <span class="booking__meridiem">am<br>pm</span>
    </div>
  </div>
</section>

</body>
</html>
```